Product Designer Business Card

Small product design, engineering and prototyping firm in need of a clean, professional business card design. To support our 3D design and drawing services, we offer 3D printing, molding, and casting of plastics, silicones, resins, etc. Our logo can still be modified/changed if necessary. The red/orange color is preferred, but may be substituted with blue or green, potentially. Either way, the colour of the logo should be match/compliment colors used throughout the design. One thought is to have the logo/contact info on one side, with the other side describing services offered, like with a small icon of 3D printer, molding, casting, and computer with a 3D model on-screen.
Industry/Entity Type
Mechanical Engineering
Contact Information for Business Card
Company: Halvick Design
Phone: 613-582-4179
Email: myles@halvickdesign.ca

```html
<!DOCTYPE html>
<html lang="en">
<head>
<meta charset="UTF-8">
<title>Halvick Design – Business Card</title>
<link href="https://fonts.googleapis.com/css2?family=Work+Sans:wght@400;500&display=swap" rel="stylesheet">
<style>
  :root {
    --page: #161616;
    --card: #232323;
    --card-edge: #2c2c2c;
    --silver: #b9b9b9;
    --silver-soft: #9a9a9a;
    --icon-fill: #3a3a3a;
  }
  * { box-sizing: border-box; margin: 0; padding: 0; }
  html, body {
    width: 1200px; height: 900px; overflow: hidden;
    background: var(--page);
    font-family: "Work Sans", Arial, sans-serif;
    color: var(--silver);
  }
  .stage {
    width: 1200px; height: 900px;
    display: flex; flex-direction: column; align-items: center; justify-content: center; gap: 40px;
  }
  .card {
    width: 640px; height: 366px;
    background: linear-gradient(135deg, var(--card) 0%, var(--card) 60%, var(--card-edge) 100%);
    box-shadow: 0 18px 40px rgba(0,0,0,.55);
    position: relative;
  }
  .card--front {
    display: flex; align-items: center; justify-content: center;
  }
  .brand__name {
    font-size: 52px; font-weight: 500; line-height: 1.1;
    color: var(--silver); letter-spacing: 6px;
    text-align: center;
  }
  .card--back { padding: 58px 60px 0; }
  .services {
    display: flex; justify-content: center; gap: 56px;
  }
  .service { display: flex; flex-direction: column; align-items: center; gap: 14px; width: 130px; }
  .service__art {
    width: 110px; height: 100px; border-radius: 6px;
    background: linear-gradient(160deg, var(--icon-fill), #2d2d2d);
    border: 2px solid #4a4a4a;
  }
  .service__label { font-size: 20px; font-weight: 500; color: var(--silver); }
  .contact {
    display: flex; justify-content: center; align-items: center; gap: 18px;
    margin-top: 44px;
  }
  .contact__person { text-align: right; }
  .contact__name { font-size: 20px; font-weight: 500; letter-spacing: .5px; }
  .contact__role { font-size: 17px; color: var(--silver-soft); }
  .contact__divider { width: 2px; height: 46px; background: var(--silver-soft); }
  .contact__lines { font-size: 18px; line-height: 1.4; }
  .contact__line { display: flex; align-items: center; gap: 7px; }
  .contact__line svg { width: 14px; height: 14px; }
</style>
</head>
<body>
<main class="stage">
  <section class="card card--front">
    <div class="brand">
      <span class="brand__name">Halvick<br>Design</span>
    </div>
  </section>

  <section class="card card--back">
    <div class="services">
      <div class="service">
        <div class="service__art" role="img" aria-label="Line icon of a molding press"></div>
        <span class="service__label">Molding</span>
      </div>
      <div class="service">
        <div class="service__art" role="img" aria-label="Line icon of a 3D printer"></div>
        <span class="service__label">3D printer</span>
      </div>
      <div class="service">
        <div class="service__art" role="img" aria-label="Icon representing casting"></div>
        <span class="service__label">Casting</span>
      </div>
    </div>

    <div class="contact">
      <div class="contact__person">
        <div class="contact__name">TREVOR HALE</div>
        <div class="contact__role">President</div>
      </div>
      <div class="contact__divider"></div>
      <div class="contact__lines">
        <div class="contact__line">
          <svg viewBox="0 0 24 24" fill="none" stroke="currentColor" stroke-width="2.2" stroke-linecap="round" stroke-linejoin="round"><path d="M5 3h4l2 5-2.5 1.5a11 11 0 0 0 6 6L16 13l5 2v4a2 2 0 0 1-2 2A16 16 0 0 1 3 5a2 2 0 0 1 2-2z"/></svg>
          <span>613-582-4179</span>
        </div>
        <div class="contact__line">
          <svg viewBox="0 0 24 24" fill="none" stroke="currentColor" stroke-width="2.2" stroke-linejoin="round"><rect x="3" y="5" width="18" height="14" rx="2"/><path d="M3 7l9 6 9-6"/></svg>
          <span>myles@halvickdesign.ca</span>
        </div>
      </div>
    </div>
  </section>
</main>
</body>
</html>
```